Cardiology Clinic Information Flyer

I have re uploaded all files. The size of our flyer will be a folded 8 1/2 by 11 page to come out measuring 5 1/2 by 8 1/2. Please make sure it fits this sizing.

Make sure each provider is matched to their picture and their profile information. Please format text as is written and separated as is for each topic.

For the back where you list the services we provide please separate as is on the attached and format text as is written and separated as is listed. If you need more space to list them you can adjust the size of the map.

Target Market(s)

Patients and other medical professionals

Industry/Entity Type

Healthcare

Font styles to use
Serif

Colors

Designer to choose colors to be used in the design.

Requirements
Must have
• Clinic Logo, provider pictures, bio on each provider, list of services offered, website, address, phone number, facebook page.

```html
<!DOCTYPE html>
<html lang="en">
<head>
<meta charset="utf-8">
<title>Cardiology Clinic – Provider Spread</title>
<link rel="stylesheet" href="https://fonts.googleapis.com/css2?family=Poppins:wght@400;500;600;700&display=swap">
<style>
  :root{
    --bg:#e4e5e8;
    --paper:#f7f7f7;
    --red:#c8141c;
    --red-dark:#8f0d12;
    --black:#262626;
    --grey:#5a5a5a;
    --ink:#3a3a3a;
    --photo-a:#6b6f78;
    --photo-b:#2d3038;
  }
  *{box-sizing:border-box;margin:0;padding:0}
  html,body{width:1200px;height:840px;overflow:hidden;background:var(--bg)}
  body{font-family:"Poppins",sans-serif;color:var(--ink)}
  .spread{position:absolute;left:110px;top:40px;width:980px;height:760px;display:flex;box-shadow:0 10px 30px rgba(0,0,0,.18)}
  .page{position:relative;width:490px;height:760px;background:var(--paper);overflow:hidden}
  .page--left{border-right:1px solid #d8d8d8}
  .page__bands{position:absolute;left:0;top:0;width:100%;height:100%;z-index:0}
  .provider{position:absolute;z-index:1;font-size:9.6px;line-height:1.38}
  .provider--right{text-align:right}
  .provider__photo{width:80px;height:86px;border:3px solid #fff;box-shadow:0 1px 3px rgba(0,0,0,.35);background:linear-gradient(160deg,var(--photo-a),var(--photo-b));margin-bottom:8px}
  .provider--right .provider__photo{margin-left:auto}
  .provider__name{color:var(--red);font-weight:700;font-size:14.5px;line-height:1.2}
  .provider__summary{font-weight:600;color:var(--black);font-size:10.2px;margin-bottom:2px}
  .provider__label{font-weight:700;color:var(--black);font-size:10.2px}
  .provider__training{list-style:none;margin:2px 0 6px}
  .provider__training li{position:relative;padding-left:10px}
  .provider__training li::before{content:"";position:absolute;left:0;top:5px;width:5px;height:5px;border-radius:50%;background:var(--red)}
  .provider--right .provider__training li{padding-left:0;padding-right:10px}
  .provider--right .provider__training li::before{left:auto;right:0}
  .provider__affiliations-title{color:var(--red);font-weight:700;font-size:10.4px}
  .provider__affiliations{list-style:none;color:var(--red);font-weight:700;font-size:10.4px;line-height:1.3}
</style>
</head>
<body>
<main class="spread">
  <section class="page page--left">
    <svg class="page__bands" viewBox="0 0 490 760" aria-hidden="true">
      <polygon points="300,0 360,0 490,130 490,190" fill="var(--red)"/>
      <polygon points="250,0 290,0 490,170 490,205" fill="var(--black)"/>
      <polygon points="360,0 490,0 490,115" fill="var(--red-dark)"/>
      <polygon points="0,600 0,640 200,760 260,760" fill="var(--red)"/>
      <polygon points="0,655 0,675 140,760 175,760" fill="var(--black)"/>
      <polygon points="0,690 0,760 120,760" fill="var(--red-dark)"/>
    </svg>

    <article class="provider" style="left:34px;top:120px;width:232px">
      <div class="provider__photo" role="img" aria-label="Portrait photo of Dr. Ravi Mehta"></div>
      <h2 class="provider__name">Ravi Mehta, MD</h2>
      <p class="provider__summary">Specializes in Interventional Cardiology, Nuclear Cardiology and Vascular Disease. Board Certified in Interventional Cardiology, Cardiovascular Disease, Nuclear Cardiology and Internal Medicine. Has been practicing since July of 2002. Completed the following training:</p>
      <ul class="provider__training">
        <li>Interventional Cardiology Fellowship at the Eastbrook College of Medicine</li>
        <li>Cardiovascular Disease Fellowship at the Eastbrook College of Medicine</li>
        <li>Internal Medicine Residency at Eastbrook General Hospital</li>
        <li>Graduated Medical School in 1990 from Westfield Medical College in India</li>
      </ul>
      <p class="provider__affiliations-title">Hospital Affiliations:</p>
      <ul class="provider__affiliations">
        <li>Bayside Regional Medical Center</li>
        <li>Bayside Southeast Hospital</li>
        <li>Lakeshore Methodist Hospital</li>
        <li>Kinsley Healthcare</li>
        <li>Keystone Healthcare</li>
        <li>Southpoint Memorial Hospital</li>
      </ul>
    </article>

    <article class="provider provider--right" style="left:272px;top:300px;width:190px">
      <div class="provider__photo" role="img" aria-label="Portrait photo of Dr. Vikram Desai"></div>
      <h2 class="provider__name">Vikram Desai, MD</h2>
      <p class="provider__summary">Specializes in Cardiovascular Diseases. Board Certified in Internal Medicine. Practicing since July 1976.</p>
      <p class="provider__label">Education:</p>
      <ul class="provider__training">
        <li>Completed Cardiovascular Disease Fellowship at Kingsbridge Medical Center, New York</li>
        <li>Completed Internal Medicine Residency at the Veterans Medical Center</li>
        <li>St. Agnes Hospital Internship</li>
        <li>Graduated Medical School from St. Columba Medical College in India</li>
      </ul>
      <p class="provider__affiliations-title">Hospital Affiliations:</p>
      <ul class="provider__affiliations">
        <li>Bayside Regional Medical Center</li>
      </ul>
    </article>
  </section>

  <section class="page page--right">
    <svg class="page__bands" viewBox="0 0 490 760" aria-hidden="true">
      <polygon points="0,0 150,0 0,95" fill="var(--red)"/>
      <polygon points="300,0 490,0 490,100" fill="var(--red)"/>
      <polygon points="250,0 285,0 490,115 490,140" fill="var(--black)"/>
      <polygon points="0,690 0,720 70,760 120,760" fill="var(--black)"/>
      <polygon points="0,730 0,760 55,760" fill="var(--grey)"/>
      <polygon points="250,760 490,680 490,705 320,760" fill="var(--red)"/>
      <polygon points="380,760 490,725 490,760" fill="var(--red-dark)"/>
    </svg>

    <article class="provider" style="left:32px;top:95px;width:300px">
      <div class="provider__photo" role="img" aria-label="Portrait photo of Dr. Anjali Rao"></div>
      <h2 class="provider__name">Anjali Rao, MD</h2>
      <p class="provider__summary">Specializes in Interventional Cardiology, Cardiovascular Disease, Nuclear Cardiology, and Echocardiography. Board Certified in Interventional Cardiology, Cardiovascular Disease, Nuclear Cardiology, Echocardiography, and Internal Medicine. Practicing since July of 2015</p>
      <p class="provider__label">Education:</p>
      <ul class="provider__training">
        <li>Interventional Cardiology Fellowship at Harlow University</li>
        <li>Cardiovascular Disease Fellowship at Crestwood General Hospital</li>
        <li>Advanced Heart Failure and Heart Transplantation at Northgate University Health System</li>
        <li>Internal Medicine Residency at Ridgemont Hospital</li>
        <li>Graduated Medical School at R.K. Medical College in India</li>
      </ul>
      <p class="provider__affiliations-title">Hospital Affiliations:</p>
      <ul class="provider__affiliations">
        <li>Bayside Regional Medical Center</li>
        <li>Lakeshore Methodist Hospital</li>
        <li>Kinsley Healthcare</li>
        <li>Keystone Healthcare</li>
        <li>Southpoint Memorial Hospital</li>
        <li>St. Anselm Medical Center</li>
      </ul>
    </article>

    <article class="provider provider--right" style="left:210px;top:385px;width:250px">
      <div class="provider__photo" role="img" aria-label="Portrait photo of Dr. Arjun Kapoor"></div>
      <h2 class="provider__name">Arjun Kapoor, MD</h2>
      <p class="provider__summary">Specializes in Cardiovascular Disease<br>Board Certified in Internal Medicine</p>
      <p class="provider__label">Education:</p>
      <ul class="provider__training">
        <li>Completed Cardiovascular Disease Fellowship at Fairview Health in Fairview, TX</li>
        <li>Completed Internal Medicine Residency at Fairview Health in Fairview, TX</li>
        <li>Graduated Medical School from Plainsview University Health Sciences Center School of Medicine</li>
      </ul>
      <p class="provider__affiliations-title">Hospital Affiliations:</p>
      <ul class="provider__affiliations">
        <li>Bayside Regional Medical Center</li>
        <li>Lakeshore Methodist Hospital</li>
      </ul>
    </article>
  </section>
</main>
</body>
</html>
```